Kestrel Bay - A new Australian wine brand; label design brief

Design a rectangular wine-bottle label - one feature design with 6x change outs for the 6x types of wines eg Mascato, Shiraz, Sauvignon Blanc

Company name: Kestrel Bay
Who are we?
We are Kestrel (K) Bay - a premium Australian wine company exporting to Vietnam. A brand created in Australia ‘the lucky country’ sharing it’s premium 6 varietals and bringing luck to those drinking in Vietnam.

What are we? (Product attributes)
6 Varieties of wine (Kestrel Bay always there for you to help at any occasion)
6 wines to be shared and create more stories
6 premium Australian wine products

Target Market(s)

Vietnamese locals buying at supermarkets

Colors

Designer to choose colors to be used in the design.

Requirements
Must have
• Design considerations:
• Simple, bold and clean design for quick recognition
• Must stand out on retail shelf (English is not the first language)
• (see attachment for typical Retail shelf)
• Create a distinct 6-colour palette to identify the varietal and provide retailing ease
• Mandatories to include
• - label on a black background and use of gold font
• - Map outline of Australia
• - The type of Wine variety with a matching colour
• - Include the word: “Premium” (as a quality guarantee)
Nice to have
• What makes us distinct / special?
• (Brand tone)
• Distinctly Australian (quality) and premium
• Bold and clean – must stand out at retail on a cluttered shelf space
• Easy to choose – simple colour coded varieties
• Easy to drink – safe, reliable, product of Australia
• Lucky – promote 6 (6 = promise of hope & prosperity in Vietnam)
Should not have
• Busy, fussy, intricate designs
• Complex language

```html
<!DOCTYPE html>
<html lang="en">
<head>
<meta charset="utf-8">
<title>Kestrel Bay – Premium Varietal Labels</title>
<link rel="stylesheet" href="https://fonts.googleapis.com/css2?family=Cinzel:wght@400&family=Pinyon+Script&family=Montserrat:wght@600&display=swap">
<style>
  :root {
    --page: #ffffff;
    --label-bg: #1b1a1e;
    --frame-line: #8a8a8c;
    --gold: #c9a600;
    --map-tone-1: rgba(201, 166, 0, 0.20);
    --map-tone-2: rgba(201, 166, 0, 0.06);
    --brand-white: #f4f4f4;
    --band-text: #1b1a1e;
    --chardonnay: #7ea04c;
    --moscato: #9a5aa3;
    --shiraz: #6a98cf;
    --sauvignon-blanc: #de7462;
    --merlot: #a0a0a2;
    --cabernet: #d3b300;
  }
  * { box-sizing: border-box; margin: 0; padding: 0; }
  html, body { width: 1200px; height: 848px; overflow: hidden; background: var(--page); }
  .label-range { position: relative; width: 1200px; height: 848px; }
  .label {
    position: absolute;
    width: 320px;
    height: 360px;
    background: var(--label-bg);
  }
  .label::before {
    content: "";
    position: absolute;
    inset: 6px 6px 0 6px;
    border: 1px solid var(--frame-line);
    border-bottom: none;
    opacity: .7;
  }
  .col-1 { left: 59px; } .col-2 { left: 439px; } .col-3 { left: 818px; }
  .row-1 { top: 35px; }  .row-2 { top: 447px; }

  .brand-dot {
    position: absolute;
    left: 50%;
    top: 42px;
    width: 40px;
    height: 40px;
    margin-left: -20px;
    border-radius: 50%;
    background: var(--gold);
  }
  .map-area {
    position: absolute;
    left: 78px;
    top: 122px;
    width: 168px;
    height: 152px;
    border-radius: 40% 46% 42% 38%;
    background: radial-gradient(ellipse at 50% 50%, var(--map-tone-1), var(--map-tone-2) 70%, transparent 100%);
  }
  .brand-name {
    position: absolute;
    left: 0; right: 0;
    top: 174px;
    text-align: center;
    font-family: "Cinzel", serif;
    font-weight: 400;
    font-size: 36px;
    line-height: 48px;
    letter-spacing: 2px;
    color: var(--brand-white);
    white-space: nowrap;
  }
  .quality-mark {
    position: absolute;
    left: 26px; right: 26px;
    top: 288px;
    display: flex;
    align-items: center;
    gap: 10px;
  }
  .quality-mark .rule { flex: 1; height: 1px; background: var(--gold); opacity: .8; }
  .quality-mark .word {
    font-family: "Pinyon Script", cursive;
    font-size: 27px;
    color: var(--gold);
    line-height: 1;
  }
  .varietal-band {
    position: absolute;
    left: 0; right: 0; bottom: 0;
    height: 29px;
    display: flex;
    align-items: center;
    justify-content: center;
    font-family: "Montserrat", sans-serif;
    font-weight: 600;
    font-size: 16px;
    letter-spacing: 3.5px;
    color: var(--band-text);
    white-space: nowrap;
  }
  .band-chardonnay { background: var(--chardonnay); }
  .band-moscato { background: var(--moscato); }
  .band-shiraz { background: var(--shiraz); }
  .band-sauvignon-blanc { background: var(--sauvignon-blanc); font-size: 15px; letter-spacing: 2.5px; }
  .band-merlot { background: var(--merlot); }
  .band-cabernet { background: var(--cabernet); font-size: 14px; letter-spacing: 2px; }
</style>
</head>
<body>
<main class="label-range">

  <section class="label col-1 row-1">
    <span class="brand-dot"></span>
    <div class="map-area" role="img" aria-label="Gold line outline map of Australia"></div>
    <h2 class="brand-name">Kestrel Bay</h2>
    <div class="quality-mark"><span class="rule"></span><span class="word">Premium</span><span class="rule"></span></div>
    <div class="varietal-band band-chardonnay">CHARDONNAY</div>
  </section>

  <section class="label col-2 row-1">
    <span class="brand-dot"></span>
    <div class="map-area" role="img" aria-label="Gold line outline map of Australia"></div>
    <h2 class="brand-name">Kestrel Bay</h2>
    <div class="quality-mark"><span class="rule"></span><span class="word">Premium</span><span class="rule"></span></div>
    <div class="varietal-band band-moscato">MASCATO</div>
  </section>

  <section class="label col-3 row-1">
    <span class="brand-dot"></span>
    <div class="map-area" role="img" aria-label="Gold line outline map of Australia"></div>
    <h2 class="brand-name">Kestrel Bay</h2>
    <div class="quality-mark"><span class="rule"></span><span class="word">Premium</span><span class="rule"></span></div>
    <div class="varietal-band band-shiraz">SHIRAZ</div>
  </section>

  <section class="label col-1 row-2">
    <span class="brand-dot"></span>
    <div class="map-area" role="img" aria-label="Gold line outline map of Australia"></div>
    <h2 class="brand-name">Kestrel Bay</h2>
    <div class="quality-mark"><span class="rule"></span><span class="word">Premium</span><span class="rule"></span></div>
    <div class="varietal-band band-sauvignon-blanc">SAUVIGNON BLANC</div>
  </section>

  <section class="label col-2 row-2">
    <span class="brand-dot"></span>
    <div class="map-area" role="img" aria-label="Gold line outline map of Australia"></div>
    <h2 class="brand-name">Kestrel Bay</h2>
    <div class="quality-mark"><span class="rule"></span><span class="word">Premium</span><span class="rule"></span></div>
    <div class="varietal-band band-merlot">MERLOT</div>
  </section>

  <section class="label col-3 row-2">
    <span class="brand-dot"></span>
    <div class="map-area" role="img" aria-label="Gold line outline map of Australia"></div>
    <h2 class="brand-name">Kestrel Bay</h2>
    <div class="quality-mark"><span class="rule"></span><span class="word">Premium</span><span class="rule"></span></div>
    <div class="varietal-band band-cabernet">CABERNET SAUVIGNON</div>
  </section>

</main>
</body>
</html>
```